Plakat-Design für einen Pflegedienst
Zielgruppe
Unter Pflegedienst besteht jetzt seit 10 Jahren, Dazu würden wir gerne ein Werbeplakat an verschiedenen Standpunkten veröffentlichen. Draus sollte hervorgehen, dass wir 10 Jahre bestehen Bilder sollten aus den Portalen verwendet werden. Der Slogan könnte vielleicht lauten:
Seit 10 Jahren rund um die Uhr für Sie im Einsatz.
oder gerne auch eine andere Idee für den Slogan.
Die Plakate sollen bei 468 Aushang veröffentlicht werden. Da wir zwei Filialen betrieben, müssten zwei verschiedene Varianten mit zwei Logos und Telefonnummern erstellt werden.
Aufgabenstellung
Das Plakat sollte modern und elegant sein.

```html
<!DOCTYPE html>
<html lang="de">
<head>
<meta charset="utf-8">
<title>Plakat – Pflegedienst 10 Jahre</title>
<link rel="stylesheet" href="https://fonts.googleapis.com/css2?family=Bebas+Neue&family=League+Spartan:wght@700&family=Lato:wght@700&display=swap">
<style>
  :root {
    --page-bg: #ffffff;
    --peach: #f5c8a5;
    --teal-band: #33a0ad;
    --teal-text: #1ea5b3;
    --teal-dark: #0f5b63;
    --scrubs: #2aa3ad;
    --scrubs-deep: #1d8c96;
    --label-white: #f5f5f5;
    --ink: #1c1c1c;
    --badge-gold: #f0a640;
    --badge-cream: #fbe7d3;
    --badge-brown: #b8651f;
    --badge-red: #e0485c;
  }
  * { margin: 0; padding: 0; box-sizing: border-box; }
  html, body {
    width: 1200px; height: 800px; overflow: hidden;
    background: var(--page-bg);
  }
  .poster {
    position: absolute;
    left: 330px; top: 17px;
    width: 540px; height: 766px;
    background: var(--peach);
    overflow: hidden;
  }
  .hero-photo {
    position: absolute; left: 241px; top: 70px;
    width: 299px; height: 281px;
    background: linear-gradient(160deg, var(--scrubs) 0%, var(--scrubs-deep) 100%);
    border-radius: 120px 0 0 0;
  }
  .tag {
    position: absolute;
    background: var(--label-white);
    color: var(--teal-text);
    font-family: 'Bebas Neue', sans-serif;
    font-size: 38px;
    line-height: 1;
    padding: 6px 14px 2px;
    letter-spacing: 1px;
    white-space: nowrap;
    transform-origin: center;
  }
  .tag--role { left: 28px; top: 158px; transform: rotate(31deg); }
  .tag--hero { left: 22px; top: 259px; transform: rotate(21deg); font-size: 40px; }
  .claim-band {
    position: absolute; left: 0; top: 351px;
    width: 540px; height: 275px;
    background: var(--teal-band);
  }
  .claim {
    position: absolute; left: 0; top: 383px; width: 540px;
    text-align: center;
    color: var(--label-white);
    font-family: 'League Spartan', sans-serif;
    font-weight: 700;
    font-size: 53px;
    line-height: 64px;
    white-space: nowrap;
  }
  .badge-label {
    position: absolute;
    font-family: 'Bebas Neue', sans-serif;
    color: var(--teal-text);
    line-height: 1;
    text-align: center;
    white-space: nowrap;
  }
  .badge-label--skill {
    left: 148px; top: 534px; width: 284px; height: 44px;
    background: var(--peach);
    font-size: 36px; padding-top: 6px;
  }
  .badge-label--years {
    left: 110px; top: 578px; width: 351px; height: 65px;
    background: var(--label-white);
    font-size: 62px; padding-top: 5px;
  }
  .logo-slot {
    position: absolute; left: 41px; top: 671px;
    width: 99px; height: 63px;
    background: var(--label-white);
    font-family: 'Lato', sans-serif; font-weight: 700;
    color: var(--ink);
    font-size: 21px; letter-spacing: 2px; line-height: 26px;
    text-align: center; padding-top: 6px;
  }
  .contact {
    position: absolute; left: 174px; top: 653px; width: 240px;
    text-align: center;
    font-style: normal;
    font-family: 'League Spartan', sans-serif; font-weight: 700;
    color: var(--teal-dark);
    font-size: 23px; line-height: 30.5px;
  }
  .service-seal { position: absolute; left: 443px; top: 658px; }
  .service-seal text {
    font-family: 'League Spartan', sans-serif; font-weight: 700;
    font-size: 15px; fill: var(--badge-brown);
  }
</style>
</head>
<body>
  <main class="poster">
    <div class="hero-photo" role="img" aria-label="Foto: Pflegekraft in türkisfarbener Berufskleidung mit Mundschutz in Heldenpose, Faust nach oben gestreckt"></div>
    <div class="tag tag--role">PFLEGENDE*R</div>
    <div class="tag tag--hero">SUPERHELD*IN</div>

    <section class="claim-band"></section>
    <h1 class="claim">RUND UM DIE UHR<br>FÜR SIE IM EINSATZ!</h1>
    <div class="badge-label badge-label--skill">PFLEGEKOMPETENZ</div>
    <div class="badge-label badge-label--years">SEIT 10 JAHREN</div>

    <div class="logo-slot">IHR<br>LOGO</div>
    <address class="contact">Kontaktdaten<br>Adresse<br>Telefonnummer</address>
    <svg class="service-seal" width="60" height="94" viewBox="0 0 60 94" aria-label="Rund um die Uhr, 24/7">
      <polygon points="17,48 7,90 18,82 27,92 31,52" fill="var(--badge-red)"/>
      <polygon points="43,48 53,90 42,82 33,92 29,52" fill="var(--badge-red)"/>
      <circle cx="30" cy="31" r="29" fill="var(--badge-gold)"/>
      <circle cx="30" cy="31" r="19" fill="var(--badge-cream)"/>
      <text x="30" y="36" text-anchor="middle">24/7</text>
    </svg>
  </main>
</body>
</html>
```